Quorvel Landing page redesign

We are looking for a landing page redesign before we officially launch. We want to incorporate the information already on the site at www.Quorvel-example.com landing page but make it more inviting. There needs to be a sign up section along with clearly stating what we do. Having a place for sample profiles and linking to our blog and podcast is option. More information about all we will be doing is at Quorvel is on the landing page and also on the blog.

Target Market(s)

35 years old and up.

Coding

Coded - Design and coding required

Number of Pages Required

1 page

Requirements
Must have
• The top bar and the bottom bar (with the privacy policy, etc)
• Sign in/up section.
• I don't want to give to much here because I want designers to be creative.
Nice to have
• Prefer not to have a landing page that requires a lot of scrolling at all.

```html
<!DOCTYPE html>
<html lang="en">
<head>
<meta charset="utf-8">
<title>Quorvel</title>
<link href="https://fonts.googleapis.com/css2?family=Lato:wght@400;700;900&display=swap" rel="stylesheet">
<style>
:root{
  --navy:#141c3d;
  --ink:#1b2238;
  --hero-top:#4cb0d6;
  --hero-bottom:#2e82ab;
  --panel:#283c46;
  --btn-blue:#1a8ae0;
  --btn-blue-dark:#0f6fc2;
  --icon-blue:#21638f;
  --line:#444a50;
  --footer:#272c3a;
  --footer-text:#a9adb8;
  --white:#ffffff;
}
*{box-sizing:border-box;margin:0;padding:0}
html,body{width:1009px;height:1200px;overflow:hidden;background:var(--white)}
body{position:relative;font-family:'Lato',sans-serif;color:var(--ink)}
.abs{position:absolute}

.topbar{left:0;top:0;width:1009px;height:43px;background:var(--navy)}
.sample-link{top:12px;display:flex;align-items:center;gap:8px;color:var(--white);font-weight:700;font-size:14px;letter-spacing:.2px}
.sample-link svg{width:19px;height:19px}

.header{left:0;top:43px;width:1009px;height:67px;background:var(--white)}
.brand{left:64px;top:62px;display:flex;align-items:center;gap:10px}
.brand-mark{width:14px;height:14px;background:var(--ink)}
.brand-name{font-size:24px;font-weight:700;color:var(--ink);line-height:1}
.nav{top:70px;font-weight:700;font-size:16px;color:var(--ink);letter-spacing:.3px}

.hero{left:0;top:110px;width:1009px;height:402px;background:linear-gradient(180deg,var(--hero-top),var(--hero-bottom))}
.preview{left:103px;top:177px;width:374px;height:253px;border:2px solid var(--navy);background:linear-gradient(135deg,#f6f6f8,#e4e6ea)}
.signin{left:602px;top:162px;width:325px;height:295px;background:var(--panel);padding:20px 24px 0 24px;color:var(--white)}
.signin h2{font-size:24px;font-weight:700;letter-spacing:.5px;line-height:1}
.field-label{font-size:15px;font-weight:700;margin-top:17px;letter-spacing:.3px}
.field{margin-top:9px;height:37px;display:flex;background:#f4f5f6;border:1px solid #dfe2e5}
.field-icon{width:36px;border-right:1px solid #cfd3d7;display:flex;align-items:center;justify-content:center}
.field-text{padding-left:11px;display:flex;align-items:center;font-size:13px;color:#5c6470;letter-spacing:.3px}
.btn-signin{margin-top:15px;height:36px;background:linear-gradient(180deg,var(--btn-blue),var(--btn-blue-dark));display:flex;align-items:center;justify-content:center;font-size:16px;font-weight:700;letter-spacing:1px}
.signup-note{margin-top:14px;text-align:center;font-size:13px;letter-spacing:.4px}
.dots{left:466px;top:482px;display:flex;gap:8px}
.dot{width:12px;height:12px;border-radius:50%;background:var(--white)}
.dot.active{background:#2a2f36}

.shadow-left{left:0;top:512px;width:332px;height:50px;background:linear-gradient(180deg,#55585e 0%,rgba(255,255,255,0) 100%);clip-path:polygon(0 0,100% 0,100% 4%,0 100%)}
.shadow-right{left:686px;top:512px;width:323px;height:50px;background:linear-gradient(180deg,#55585e 0%,rgba(255,255,255,0) 100%);clip-path:polygon(0 0,100% 0,100% 100%,0 4%)}

.pages-title{left:0;width:1009px;top:572px;text-align:center;font-size:20px;font-weight:700;letter-spacing:2px}
.pages-lead{left:0;width:1009px;top:611px;text-align:center;font-size:13px;font-weight:700;line-height:18px;letter-spacing:.2px}
.tree{left:0;top:676px;width:1009px;height:110px}
.feature{top:797px;width:150px;text-align:center;font-size:13.5px;font-weight:700;line-height:20px;letter-spacing:.6px}
.btn-start{left:399px;top:900px;width:217px;height:40px;background:var(--navy);color:var(--white);display:flex;align-items:center;justify-content:center;font-size:14.5px;font-weight:700;letter-spacing:.4px;box-shadow:0 2px 4px rgba(0,0,0,.3)}

.early{left:0;top:993px;width:1009px;height:155px;background:linear-gradient(180deg,var(--hero-top),var(--hero-bottom));text-align:center;color:var(--white)}
.early h3{margin-top:34px;font-size:21px;font-weight:700;letter-spacing:2px}
.early p{margin-top:10px;font-size:13px;font-weight:700;letter-spacing:.5px;color:#d8eef8}
.subscribe{left:339px;top:1094px;width:337px;height:31px;display:flex;border:2px solid #2a5c7a}
.subscribe-input{flex:1;background:var(--white);display:flex;align-items:center;padding-left:13px;font-size:13.5px;color:#7a808a;letter-spacing:.4px}
.subscribe-btn{width:86px;background:var(--navy);color:var(--white);display:flex;align-items:center;justify-content:center;font-size:12.5px;font-weight:700;letter-spacing:1px}

.footer{left:0;top:1148px;width:1009px;height:52px;background:linear-gradient(180deg,#3b3140,var(--footer));display:flex;align-items:center;justify-content:center;gap:8px;font-size:12.5px;color:var(--footer-text)}
</style>
</head>
<body>
<div class="abs topbar"></div>
<div class="abs sample-link" style="left:542px">
  <svg viewBox="0 0 20 20"><circle cx="10" cy="10" r="9" fill="none" stroke="#fff" stroke-width="1.5"/><circle cx="10" cy="8" r="3.2" fill="#fff"/><path d="M4.5 15.5c1.5-3 9.5-3 11 0" fill="#fff"/></svg>
  Sample Legacy Profile
</div>
<div class="abs sample-link" style="left:744px">
  <svg viewBox="0 0 20 20"><circle cx="10" cy="10" r="9" fill="none" stroke="#fff" stroke-width="1.5"/><circle cx="10" cy="8" r="3.2" fill="#fff"/><path d="M4.5 15.5c1.5-3 9.5-3 11 0" fill="#fff"/></svg>
  Sample Quorvel Profile
</div>

<div class="abs header"></div>
<div class="abs brand">
  <span class="brand-mark"></span>
  <span class="brand-name">Quorvel</span>
</div>
<div class="abs nav" style="left:776px">BLOG</div>
<div class="abs nav" style="left:852px">PODCAST</div>

<div class="abs hero"></div>
<div class="abs preview" role="img" aria-label="Preview of a family tree chart with connected name boxes"></div>
<div class="abs signin">
  <h2>SIGN IN HERE</h2>
  <div class="field-label">Email</div>
  <div class="field">
    <div class="field-icon"><svg width="18" height="12" viewBox="0 0 18 12"><rect x=".5" y=".5" width="17" height="11" fill="#8c939b"/><path d="M.5 .5 9 7l8.5-6.5" fill="none" stroke="#eef0f2" stroke-width="1.2"/></svg></div>
    <div class="field-text">Type Your Email</div>
  </div>
  <div class="field-label">Password</div>
  <div class="field">
    <div class="field-icon"><svg width="13" height="17" viewBox="0 0 13 17"><path d="M3 8V5a3.5 3.5 0 0 1 7 0v3" fill="none" stroke="#8c939b" stroke-width="1.8"/><rect x="1" y="8" width="11" height="8" fill="#8c939b"/></svg></div>
    <div class="field-text">Type Your Password</div>
  </div>
  <div class="btn-signin">SIGN IN</div>
  <div class="signup-note">You have not yet account Signup here?</div>
</div>
<div class="abs dots"><span class="dot"></span><span class="dot"></span><span class="dot"></span><span class="dot active"></span></div>

<div class="abs shadow-left"></div>
<div class="abs shadow-right"></div>

<div class="abs pages-title">Quorvel Pages</div>
<div class="abs pages-lead">Build multiple Quorvel pages through one account for yourself,<br>your family and to keep loved one's legacies alive.</div>

<svg class="abs tree" viewBox="0 0 1009 110">
  <path d="M480 57a17 17 0 0 1 5-33a20 20 0 0 1 37-3a17 17 0 0 1 15 36z" fill="#21638f"/>
  <g fill="#fff">
    <rect x="487" y="26" width="34" height="7" rx="3.5"/>
    <rect x="487" y="36" width="34" height="7" rx="3.5"/>
    <rect x="487" y="46" width="34" height="7" rx="3.5"/>
  </g>
  <g fill="#21638f"><circle cx="491" cy="29.5" r="1.6"/><circle cx="491" cy="39.5" r="1.6"/><circle cx="491" cy="49.5" r="1.6"/></g>
  <g fill="none" stroke="#444a50" stroke-width="4">
    <path d="M504 57v45"/>
    <path d="M214 102V75h580v27"/>
    <path d="M353 75v27M645 75v27"/>
  </g>
</svg>

<div class="abs feature" style="left:132px">Create Timelines,<br>Maps, Family<br>Trees</div>
<div class="abs feature" style="left:277px">Share Family<br>Stories, History<br>and more</div>
<div class="abs feature" style="left:433px;line-height:25px">Memorialize<br>Loved Ones</div>
<div class="abs feature" style="left:573px;line-height:25px">Control<br>Your Privacy</div>
<div class="abs feature" style="left:719px">No Ads, No Like<br>Buttons<br>No News Feeds</div>

<div class="abs btn-start">Get Started</div>

<div class="abs early">
  <h3>Become An Early User</h3>
  <p>For Daily News Update Signuo here.</p>
</div>
<div class="abs subscribe">
  <div class="subscribe-input">Type your Email</div>
  <div class="subscribe-btn">Subcribe</div>
</div>

<div class="abs footer">
  <span>Privacy Policy</span><span>Terms of Use</span><span>Data Tracking Policy</span><span>Submit Feedback</span><span>Quorvel © 2017</span>
</div>
</body>
</html>
```